plumbing & gas fitting business card design

We need a business card design for a plumbing & gas fitting company. The company covers commercial, domestic and maintenance work. We would like a modern design communicating efficiency and sophistication. preferred colours would include (red grey & black) or (green grey & black). Please DO NOT include any water droplets.

Industry/Entity Type

Business

Contact Information for Business Card

Vortig Plumbing & Gas, Commercial Domestic & Maintenance, licence no. 617394K, ABN 47215830962, Phone 0417382956, Email vortigplumbingandgas@corvanet.com

```html
<!DOCTYPE html>
<html lang="en">
<head>
<meta charset="utf-8">
<title>Vortig Plumbing &amp; Gas — Business Card</title>
<link rel="stylesheet" href="https://fonts.googleapis.com/css2?family=Inter:wght@300&display=swap">
<style>
  :root {
    --brand-red: #ee1c1c;
    --slate-grey: #87908f;
    --ink: #111111;
    --paper: #ffffff;
  }
  * { margin: 0; padding: 0; box-sizing: border-box; }
  html, body {
    width: 1200px;
    height: 660px;
    overflow: hidden;
    background: var(--paper);
  }
  .card {
    position: relative;
    width: 1200px;
    height: 660px;
    background: var(--paper);
    font-family: "Inter", Arial, sans-serif;
    font-weight: 300;
    overflow: hidden;
  }
  .company-name,
  .services {
    position: absolute;
    left: 0;
    width: 1200px;
    text-align: center;
    white-space: nowrap;
    line-height: 1;
    font-weight: 300;
  }
  .company-name {
    top: 58px;
    font-size: 62px;
    letter-spacing: 0.03em;
    color: var(--brand-red);
  }
  .services {
    top: 298px;
    font-size: 47px;
    letter-spacing: 0.228em;
    padding-left: 0.228em;
    color: var(--slate-grey);
  }
  .contact {
    position: absolute;
    top: 571px;
    font-size: 36px;
    line-height: 45px;
    color: var(--ink);
    white-space: nowrap;
  }
  .contact--primary { left: 0; }
  .contact--registration { right: 0; }
</style>
</head>
<body>
  <main class="card">
    <h1 class="company-name">Vortig Plumbing &amp; Gas</h1>
    <p class="services">commercial, domestic &amp; maintenance</p>
    <div class="contact contact--primary">
      <p class="contact-phone">Phone number: 0417382956</p>
      <p class="contact-email">Email: vortigplumbingandgas@corvanet.com</p>
    </div>
    <div class="contact contact--registration">
      <p class="contact-licence">licence no. 617394K</p>
      <p class="contact-abn">ABN.&nbsp; 47215830962</p>
    </div>
  </main>
</body>
</html>
```